Business Cards for Valet Parking Company
Modern & Hospitality Oriented
Business Cards for Valet Parking Company - Automotive
Creative Brief
Simple
Colin Marsh
Owner & President
48270 E 9 Pine Avenue Suite 400 Farmington Hills, MI 48127
colin@orbitparkco.com
www.orbitparkco.com
On back of card: Anticipate, Invite & Engage

```html
<!DOCTYPE html>
<html lang="en">
<head>
<meta charset="utf-8">
<title>Orbit Parking Co — Business Card</title>
<link href="https://fonts.googleapis.com/css2?family=Exo+2:wght@400;500;600&display=swap" rel="stylesheet">
<style>
  :root {
    --card: #ffffff;
    --ink: #2a2a2a;
    --icon: #333333;
    --icon-glyph: #ffffff;
    --accent-blue: #1f8ad0;
    --accent-yellow: #f4b400;
  }
  html, body {
    margin: 0;
    padding: 0;
    width: 1200px;
    height: 816px;
    overflow: hidden;
    background: var(--card);
  }
  .card {
    position: relative;
    width: 1200px;
    height: 816px;
    background: var(--card);
    font-family: "Exo 2", sans-serif;
    color: var(--ink);
  }
  .rule {
    position: absolute;
    left: 70px;
    height: 7px;
    background: var(--ink);
  }
  .rule-top { top: 170px; width: 520px; }
  .rule-bottom { top: 345px; width: 430px; }

  .identity {
    position: absolute;
    left: 80px;
    top: 222px;
    display: flex;
    align-items: center;
    gap: 26px;
  }
  .person-name {
    margin: 0;
    font-size: 36px;
    font-weight: 500;
    letter-spacing: 2px;
    text-transform: uppercase;
    line-height: 1.1;
  }
  .person-title {
    margin: 4px 0 0;
    font-size: 28px;
    font-weight: 400;
    letter-spacing: 2px;
  }
  .contacts {
    position: absolute;
    left: 80px;
    top: 420px;
    margin: 0;
    padding: 0;
    list-style: none;
  }
  .contact-row {
    display: flex;
    align-items: center;
    gap: 26px;
    margin-bottom: 30px;
  }
  .contact-lines {
    font-size: 25px;
    font-weight: 400;
    letter-spacing: 1.5px;
    line-height: 1.35;
  }
  .icon { flex: none; width: 60px; height: 60px; }
  .icon .disc { fill: var(--icon); }
  .icon .glyph { fill: var(--icon-glyph); }
  .icon .glyph-line { fill: none; stroke: var(--icon-glyph); stroke-width: 3; }

  .brand {
    position: absolute;
    left: 680px;
    top: 330px;
    display: flex;
    align-items: center;
    gap: 22px;
  }
  .brand-dot {
    width: 46px;
    height: 46px;
    border-radius: 50%;
    background: var(--accent-blue);
  }
  .brand-name {
    margin: 0;
    font-size: 54px;
    font-weight: 600;
    letter-spacing: 3px;
    line-height: 1.05;
    text-transform: uppercase;
    color: var(--ink);
  }
</style>
</head>
<body>
  <main class="card">
    <div class="rule rule-top"></div>

    <div class="identity">
      <svg class="icon" viewBox="0 0 60 60" aria-hidden="true">
        <circle class="disc" cx="30" cy="30" r="30"/>
        <circle class="glyph" cx="30" cy="23" r="8"/>
        <path class="glyph" d="M16 44c0-8 6-12 14-12s14 4 14 12z"/>
      </svg>
      <div>
        <h1 class="person-name">Colin Marsh</h1>
        <p class="person-title">Owner &amp; President</p>
      </div>
    </div>

    <div class="rule rule-bottom"></div>

    <ul class="contacts">
      <li class="contact-row">
        <svg class="icon" viewBox="0 0 60 60" aria-hidden="true">
          <circle class="disc" cx="30" cy="30" r="30"/>
          <rect class="glyph" x="21" y="14" width="18" height="32" rx="3"/>
          <rect class="disc" x="24" y="19" width="12" height="20"/>
        </svg>
        <div class="contact-lines">248 555 0147<br>248 555 0193</div>
      </li>
      <li class="contact-row">
        <svg class="icon" viewBox="0 0 60 60" aria-hidden="true">
          <circle class="disc" cx="30" cy="30" r="30"/>
          <rect class="glyph-line" x="16" y="18" width="28" height="19" rx="2"/>
          <rect class="glyph" x="26" y="38" width="8" height="4"/>
          <rect class="glyph" x="21" y="42" width="18" height="3"/>
        </svg>
        <div class="contact-lines">colin@orbitparkco.com<br>www.orbitparkco.com</div>
      </li>
      <li class="contact-row">
        <svg class="icon" viewBox="0 0 60 60" aria-hidden="true">
          <circle class="disc" cx="30" cy="30" r="30"/>
          <path class="glyph" d="M30 13c-7 0-12 5-12 12 0 9 12 22 12 22s12-13 12-22c0-7-5-12-12-12z"/>
          <circle class="disc" cx="30" cy="25" r="4.5"/>
        </svg>
        <div class="contact-lines">48270 E 9 Pine Avenue Suite 400<br>Farmington Hills, MI 48127</div>
      </li>
    </ul>

    <div class="brand">
      <div class="brand-dot"></div>
      <p class="brand-name">Orbit<br>Parking Co</p>
    </div>
  </main>
</body>
</html>
```